Glen Holbrook Announces his new career move! 8x5 card please.

Associate Broker GLEN HOLBROOK is proud to announce his new affiliation with m.vorlund bayshore estates, ltd.

His goal remains to meet all your real estate needs. Prepare to renew your seasonal rental for 2016...with the full support of his new office, Glen can handle your renewal seamlessly.

Prepared to purchase? With access to every property on the market...Glen can show you how easy it making your summer dreams come true can be.

Thinking about selling? m.vorlund bayshore estates, ltd. now offers the benefits of the Multiple Listing Service (MLS) to all sellers. In cooperation with MLS Sellers receive the maximum worldwide exposure, Purchasers receive a larger volume of properties to view and in cooperation with other Realtors, the transaction is handled professionally!!!!

I will send logo and photo of Glen Holbrook separately. Thank you. P-
Updates

Target Market(s)

Tenants, Sellers & Buyers

Industry/Entity Type

Broker

Font styles to use
Sans Serif

Requirements
Must have
• I attached logo and photo of Glen. Added a better photo of Glen.
Nice to have
• A photo of a property we have listed. I added a couple to choose from.
Should not have
• No Red color

```html
<!DOCTYPE html>
<html lang="en">
<head>
<meta charset="utf-8">
<title>Glen Holbrook – Announcement Postcard</title>
<link rel="stylesheet" href="https://fonts.googleapis.com/css2?family=Open+Sans:wght@400;600;700;800&family=Alegreya:ital@1&display=swap">
<style>
:root{
  --green:#08754a;
  --green-dark:#066540;
  --ink:#1f1f1f;
  --grey-text:#333;
  --panel:#e8e8ea;
  --page:#ecebe8;
  --white:#fff;
  --black-band:#1b1b1d;
}
*{box-sizing:border-box;margin:0;padding:0}
html,body{width:860px;height:1200px;overflow:hidden}
body{background:var(--page);font-family:"Open Sans",Arial,sans-serif;color:var(--ink);position:relative}

.card{position:absolute;left:82px;width:713px;background:var(--white);box-shadow:0 2px 6px rgba(0,0,0,.18);overflow:hidden}
.card--front{top:92px;height:506px;background:linear-gradient(#fff 0,#fff 290px,#e9e9eb 360px,#fff 470px)}
.card--back{top:628px;height:508px}

/* front */
.brand{position:absolute;left:32px;top:38px;display:flex;align-items:center;gap:12px}
.brand__mark{width:20px;height:20px;background:var(--green)}
.brand__name{font-weight:800;font-size:32px;letter-spacing:-1px;color:var(--ink)}

.announce{position:absolute;left:0;top:123px;width:713px;height:58px;background:var(--green);color:var(--white);padding:6px 0 0 34px;font-size:17px;line-height:23px}
.announce b{font-weight:700}
.announce-tab{position:absolute;top:113px;left:563px;width:120px;height:80px;z-index:1}
.logo-box{position:absolute;left:576px;top:116px;width:106px;height:76px;background:var(--white);display:flex;align-items:center;justify-content:center;z-index:2}
.logo-box span{width:26px;height:26px;border-radius:50%;background:var(--green)}

.goal{position:absolute;left:0;top:186px;width:713px;height:72px}
.goal p{position:absolute;left:34px;top:10px;width:620px;font-family:"Alegreya",Georgia,serif;font-style:italic;color:var(--white);font-size:15.5px;line-height:25px}

.section-title{position:absolute;left:34px;color:var(--green);font-weight:700;font-size:18px}
.section-body{position:absolute;left:34px;font-size:11.5px;line-height:15px;color:var(--grey-text)}
.purchase-title{top:274px}
.purchase-body{top:306px;width:430px}
.selling-title{top:356px}
.selling-body{top:389px;width:645px;text-align:justify}
.selling-body .short{display:block;width:330px;text-align:left}

.web{position:absolute;right:30px;top:427px;width:284px;height:34px}
.web span{position:absolute;left:0;top:0;width:284px;line-height:34px;text-align:center;color:var(--white);font-weight:700;font-size:17px;letter-spacing:.3px}
.contact{position:absolute;left:0;top:461px;width:713px;height:45px;background:var(--green);color:var(--white);font-weight:700;font-size:24px;line-height:45px;padding-left:41px;border-top:3px solid #fff}

/* back */
.back-top{position:absolute;left:0;top:0;width:713px;height:11px;background:var(--green)}
.headline{position:absolute;left:25px;top:22px;font-size:28px;color:#333;font-weight:400;letter-spacing:-.3px}
.headline b{font-weight:700;color:#333}
.headline b.accent{color:var(--green)}
.stamp{position:absolute;left:584px;top:32px;width:105px;height:108px;border-radius:8px;background:#e6e6e8}

.gallery{position:absolute;left:23px;top:68px;width:521px;height:112px;background:var(--green);display:flex;gap:3px;padding:7px}
.gallery .photo{flex:1;height:98px}
.photo--kitchen{background:linear-gradient(160deg,#8a6a45,#c9b79d 55%,#6d5a45)}
.photo--pool{background:linear-gradient(180deg,#bfd6e6 0,#e8eef0 40%,#3ea0d8 62%,#2a7fb8)}
.photo--bedroom{background:linear-gradient(170deg,#eae7e2,#cfc6bb 60%,#8b7b70)}
.photo--view{background:linear-gradient(180deg,#b9d4ea 0,#5f98c2 35%,#b7bcc0 55%,#4a6a3a 80%)}

.agent{position:absolute;left:23px;top:208px;width:396px;height:229px;background:var(--panel)}
.agent__name{position:absolute;left:10px;top:8px;font-size:20px;font-weight:700;color:#333;white-space:nowrap}
.agent__name span{font-weight:400;color:var(--green)}
.agent__portrait{position:absolute;left:10px;top:45px;width:123px;height:148px;border-radius:6px;background:linear-gradient(180deg,#a9c0cc 0,#8e8a80 45%,#3a2c28 75%,#1f1a19);border:1px solid #999}
.agent__bar{position:absolute;left:0;top:201px;width:396px;height:28px;background:var(--green);color:var(--white);font-weight:700;font-size:13px;line-height:28px;z-index:2}
.agent__bar .fax{position:absolute;left:10px}
.agent__bar .mail{position:absolute;left:156px}

.office{position:absolute;left:167px;top:252px;width:252px;height:157px;background:var(--green);border-radius:8px 0 0 0}
.office__note{position:absolute;left:1px;top:1px;width:238px;height:86px;background:var(--white);border-radius:7px;display:flex}
.office__mark{width:75px;display:flex;align-items:center;justify-content:center}
.office__mark span{width:22px;height:22px;border-radius:50%;background:var(--green)}
.office__note p{font-size:10px;line-height:13px;color:var(--green);padding-top:15px;width:155px}
.office__name{position:absolute;left:11px;top:99px;color:var(--white);font-weight:700;font-size:11.5px}
.office__addr{position:absolute;left:11px;top:121px;width:222px;color:var(--white);font-size:11.5px;line-height:15px}

.address-lines{position:absolute;left:451px;top:329px;width:232px}
.address-lines span{display:block;height:1px;background:#888;margin-bottom:35px}
.postal{position:absolute;left:122px;top:465px;font-size:10px;font-weight:600;color:#222}
</style>
</head>
<body>

<section class="card card--front">
  <div class="brand"><span class="brand__mark"></span><span class="brand__name">m.vorlund bayshore estates, ltd.</span></div>

  <svg class="announce-tab" viewBox="0 0 120 80" aria-hidden="true">
    <polygon points="0,10 13,0 13,10" fill="#3a3a3a"/>
    <polygon points="107,0 120,10 107,10" fill="#3a3a3a"/>
  </svg>
  <div class="announce">Associate Broker <b>GLEN HOLBROOK</b> is proud to announce his<br>new affiliation with <b>m.vorlund</b> bayshore estates, ltd.</div>
  <div class="logo-box"><span></span></div>

  <div class="goal">
    <svg width="713" height="72" viewBox="0 0 713 72" aria-hidden="true">
      <defs><linearGradient id="bandShade" x1="0" y1="0" x2="0" y2="1"><stop offset="0" stop-color="#3a3a3c"/><stop offset="1" stop-color="#141415"/></linearGradient></defs>
      <path d="M0 0 H713 V0 C690 4 685 40 660 60 C648 70 640 72 620 72 H0 Z" fill="url(#bandShade)"/>
    </svg>
    <p>His goal remains to meet all your real estate needs. Prepare to renew your seasonal rental for 2016...with the full support of his new office, Glen can handle your renewal seamlessly.</p>
  </div>

  <h2 class="section-title purchase-title">Prepared to purchase?</h2>
  <p class="section-body purchase-body">With access to every property on the market...Glen can show you how easy it making your summer dreams come true can be.</p>

  <h2 class="section-title selling-title">Thinking about selling?</h2>
  <p class="section-body selling-body">m.vorlund bayshore estates, ltd. now offers the benefits of the Multiple Listing Service (MLS) to all sellers. In cooperation with MLS Sellers receive the maximum worldwide exposure, Purchasers receive a larger volume of <span class="short">properties to view and in cooperation with other Realtors, the transaction is handled professionally!!!!</span></p>

  <div class="web">
    <svg width="284" height="34" viewBox="0 0 284 34" aria-hidden="true"><path d="M0 34 C14 34 14 0 34 0 H258 C272 0 274 20 284 34 Z" fill="#1b1b1d"/></svg>
    <span>www.bayshorehaven.com</span>
  </div>
  <div class="contact">Contact us: 555.210.4400, 555.318.2290 (Glen)</div>
</section>

<section class="card card--back">
  <div class="back-top"></div>
  <h1 class="headline">the fabulous homes of <b>bayshore</b> <b class="accent">haven</b></h1>
  <div class="stamp"></div>

  <div class="gallery">
    <div class="photo photo--kitchen" role="img" aria-label="Photo of a wood-panelled kitchen"></div>
    <div class="photo photo--pool" role="img" aria-label="Photo of a white house with a swimming pool"></div>
    <div class="photo photo--bedroom" role="img" aria-label="Photo of a bright bedroom"></div>
    <div class="photo photo--view" role="img" aria-label="Photo of an ocean view over the treetops"></div>
  </div>

  <div class="agent">
    <h2 class="agent__name">GLEN HOLBROOK - <span>Associate Broker</span></h2>
    <div class="agent__portrait" role="img" aria-label="Portrait photo of Glen Holbrook"></div>
    <div class="agent__bar"><span class="fax">fax: 555-210-4450</span><span class="mail">e-mail: info@bayshorehaven.com</span></div>
  </div>

  <div class="office">
    <div class="office__note">
      <div class="office__mark"><span></span></div>
      <p>Please contact us if you have any questions or need more information. New properties are always coming on the market.</p>
    </div>
    <div class="office__name">m.vorlund bayshore estates, ltd.</div>
    <div class="office__addr">on the harbor, P.O. Box 2187, Bayshore Haven, NY 10990</div>
  </div>

  <div class="address-lines"><span></span><span></span><span></span><span></span></div>
  <div class="postal">barcode &amp; postal marketing area</div>
</section>

</body>
</html>
```